Business card for apparel company. Specializing in fishing and boating performance wear. Main company name is Marlow Pelican Company, LLC brand name for apparel is TIDEWAKE. See website www.TidewakeBayline.com I will attach some logos to consider.

```html
<!DOCTYPE html>
<html lang="en">
<head>
<meta charset="utf-8">
<title>Tidewake Business Card</title>
<link rel="stylesheet" href="https://fonts.googleapis.com/css2?family=Lato:wght@400;700;900&display=swap">
<style>
  :root {
    --backdrop: #2b2f35;
    --ocean-deep: #0d2f6e;
    --ocean-mid: #1f5fb0;
    --ocean-light: #4f9ad8;
    --brand-blue: #0a6ad9;
    --brand-cyan: #1aa3e8;
    --accent-orange: #f59a12;
    --accent-sky: #3fb2ef;
    --paper: #ffffff;
  }
  * { margin: 0; padding: 0; box-sizing: border-box; }
  html, body { width: 1200px; height: 875px; overflow: hidden; }
  body {
    background: var(--backdrop);
    font-family: "Lato", sans-serif;
    position: relative;
  }
  .card {
    position: absolute;
    top: 283px;
    width: 540px;
    height: 309px;
    border-radius: 22px;
    overflow: hidden;
    box-shadow: 0 14px 34px rgba(0,0,0,0.45);
  }
  .card-front { left: 40px; }
  .card-back { left: 620px; background: var(--paper); }

  .front-photo {
    position: absolute; inset: 0;
    background:
      radial-gradient(ellipse at 20% 0%, rgba(120,190,240,0.55), transparent 55%),
      radial-gradient(ellipse at 30% 100%, rgba(10,30,70,0.8), transparent 60%),
      linear-gradient(160deg, var(--ocean-mid) 0%, var(--ocean-deep) 55%, #163d7a 100%);
  }
  .front-brand {
    position: absolute; inset: 0;
    display: flex; align-items: center; justify-content: center; gap: 14px;
  }
  .front-brand .mark-dot {
    width: 30px; height: 30px; border-radius: 50%;
    background: var(--paper);
  }
  .front-brand .brand-name {
    color: var(--paper);
    font-weight: 900;
    font-size: 62px;
    letter-spacing: 2px;
  }

  .back-art { position: absolute; inset: 0; }
  .back-brand {
    position: absolute; left: 28px; top: 200px;
    display: flex; align-items: center; gap: 9px;
  }
  .back-brand .mark-dot {
    width: 16px; height: 16px; border-radius: 50%;
    background: var(--brand-cyan);
  }
  .back-brand .brand-name {
    color: var(--brand-blue);
    font-weight: 900;
    font-size: 31px;
    letter-spacing: 1px;
    white-space: nowrap;
  }
  .contact {
    position: absolute; left: 300px; top: 40px;
    color: var(--paper);
  }
  .contact .person { font-weight: 900; font-size: 22px; letter-spacing: 0.5px; }
  .contact .role { font-size: 14px; margin-bottom: 10px; }
  .contact .line { font-size: 13px; line-height: 1.45; }
  .contact .channels { margin-top: 12px; }
  .contact .channel { display: flex; align-items: center; gap: 8px; font-size: 13px; line-height: 1.55; }
  .contact .channel svg { width: 12px; height: 12px; flex: none; }
</style>
</head>
<body>
  <section class="card card-front">
    <div class="front-photo" role="img" aria-label="Underwater photograph of a school of fish over a coral reef in deep blue water"></div>
    <div class="front-brand">
      <span class="mark-dot"></span>
      <span class="brand-name">TIDEWAKE</span>
    </div>
  </section>

  <section class="card card-back">
    <svg class="back-art" viewBox="0 0 540 309" preserveAspectRatio="none">
      <path d="M540 0 H200 C175 60 215 110 250 160 C290 215 300 260 290 309 H540 Z" fill="var(--brand-blue)"/>
      <path d="M200 0 C175 60 215 110 250 160 C290 215 300 260 290 309" fill="none" stroke="var(--accent-sky)" stroke-width="5"/>
      <path d="M188 0 C163 62 200 115 236 165 C272 218 282 262 274 309" fill="none" stroke="var(--accent-orange)" stroke-width="5"/>
    </svg>

    <div class="back-brand">
      <span class="mark-dot"></span>
      <span class="brand-name">TIDEWAKE</span>
    </div>

    <div class="contact">
      <div class="person">OWEN HARTLEY</div>
      <div class="role">Founder &amp; CEO</div>
      <div class="line">Marlow Pelican Company, LLC</div>
      <div class="line">P.O. Box 412</div>
      <div class="line">Harlow Key, Florida 34011</div>
      <div class="channels">
        <div class="channel">
          <svg viewBox="0 0 12 12"><path d="M2.5 1 L4.5 1 L5.3 3.6 L4 4.6 C4.6 6 6 7.4 7.4 8 L8.4 6.7 L11 7.5 L11 9.5 C11 10.3 10.3 11 9.5 11 C5 11 1 7 1 2.5 C1 1.7 1.7 1 2.5 1 Z" fill="#fff"/></svg>
          <span>(555) 214-0387</span>
        </div>
        <div class="channel">
          <svg viewBox="0 0 12 12"><rect x="1" y="2.5" width="10" height="7" rx="1" fill="#fff"/><path d="M1.5 3 L6 6.5 L10.5 3" fill="none" stroke="var(--brand-blue)" stroke-width="1"/></svg>
          <span>info@MarlowPelicanCo.com</span>
        </div>
        <div class="channel">
          <svg viewBox="0 0 12 12"><circle cx="6" cy="6" r="5" fill="#fff"/><path d="M1 6 H11 M6 1 C3.5 3.5 3.5 8.5 6 11 M6 1 C8.5 3.5 8.5 8.5 6 11" fill="none" stroke="var(--brand-blue)" stroke-width="0.8"/></svg>
          <span>MarlowPelicanCo.com</span>
        </div>
      </div>
    </div>
  </section>
</body>
</html>
```